Telmora Coaching flyer (women local)

Strapline: Do you want a more fulfilling and meaningful life?
Make 2015 a year for positive change

Image of an attractive woman in contemplation:

• I’ve lost my identity and wondering what life is about.

• I want more intimacy in my relationship

• I hate my career and don’t know what’s right for me

Personal Development Coaching can help you:

Testimonials from our clients:

‘I have changed the way I approach my daily life in order to achieve more for myself’.

‘Coaching has helped me change the way I think, focusing more on positive rather than negative thoughts’.

‘Without coaching, I believe that my life would have remained stagnant’.

‘ I have made the leap to set up my own business and have increased my income three fold’.

‘Coaching has helped me to grow closer than ever to my husband’.

Any relevant image and image of myself (included)

Why Telmora?

• Certified Personal Development Coach

• Experience coaching individuals wanting to effect change

Nadia is a specialist in coaching for:

• Building confidence

• Feeling motivated and getting out of a rut

• Enhancing relationships with partners or family

• Making changes in your career or business

Book your free consultation (this should stand out)

e: nadia@telmora-example.co.uk t: 0798 512 6043 w: www.telmora-example.co.uk (include logo, but change ‘Telmora Consulting’ to ‘Telmora Coaching’)
f: www.facebook.com/telmora-example.co.uk t: @ndtelmora

* Notes in brackets are only instructions and not to be included as part of the flyer.

Flyer is is A5

Please not this flyer can be double sided as I feel there will be too much text for one side. Could you use image of woman in contemplation on front but not too depressing.

```html
<!DOCTYPE html>
<html lang="en">
<head>
<meta charset="utf-8">
<title>Telmora Coaching – Flyer</title>
<link rel="stylesheet" href="https://fonts.googleapis.com/css2?family=PT+Sans:wght@400;700&family=PT+Serif:wght@700&display=swap">
<style>
  :root {
    --page-bg: #e6e8eb;
    --paper: #ffffff;
    --teal: #1b8db0;
    --sky-text: #22a3cc;
    --navy: #253e6e;
    --royal: #2f55a0;
    --body-text: #2c3550;
    --wave-dark: #2a5cab;
    --wave-mid: #3b8fd0;
    --wave-light: #6fcbe6;
    --dot: #5cc3e3;
    --badge-outer: #f5a13a;
    --badge-inner: #e85a1c;
    --badge-text: #ffffff;
    --rule: #8fd0e8;
  }
  * { box-sizing: border-box; margin: 0; padding: 0; }
  html, body { width: 1200px; height: 866px; overflow: hidden; }
  body {
    background: var(--page-bg);
    font-family: "PT Sans", Arial, sans-serif;
    color: var(--body-text);
    position: relative;
  }

  .flyer {
    position: absolute;
    width: 544px;
    height: 770px;
    background: var(--paper);
    overflow: hidden;
    box-shadow: 0 2px 8px rgba(0,0,0,.18);
  }
  .flyer--front { left: 45px; top: 38px; }
  .flyer--back { left: 608px; top: 40px; }

  .photo { position: absolute; left: 0; top: 0; width: 100%; }
  .photo--contemplation {
    height: 560px;
    background: linear-gradient(180deg, #bfe0f2 0%, #d9ecf6 30%, #b9cfd6 55%, #8ea58c 75%, #9a9582 100%);
  }
  .photo--portrait {
    height: 470px;
    background: linear-gradient(100deg, #d8c6b6 0%, #e8dccf 40%, #f1e9df 70%, #f6f1ea 100%);
  }

  .wave { position: absolute; left: 0; width: 100%; }

  .logo-box {
    position: absolute;
    background: var(--paper);
    display: flex;
    flex-direction: column;
    align-items: center;
    justify-content: center;
    gap: 6px;
  }
  .logo-box__mark { width: 14px; height: 14px; border-radius: 50%; background: var(--royal); }
  .logo-name {
    font-family: "PT Sans", Arial, sans-serif;
    font-weight: 400;
    color: var(--royal);
    text-align: center;
    line-height: 1.05;
  }
  .flyer--front .logo-box { left: 415px; top: 0; width: 113px; height: 110px; }
  .flyer--back .logo-box { left: 15px; top: 0; width: 112px; height: 118px; }
  .logo-box .logo-name { font-size: 17px; }

  .headline {
    position: absolute; left: 15px; top: 10px;
    color: var(--teal); font-weight: 700; text-transform: uppercase; line-height: 1;
  }
  .headline__lead { font-size: 37px; display: block; }
  .headline__rest { font-size: 29px; display: block; margin-top: 2px; }

  .subhead {
    position: absolute; left: 15px; top: 118px;
    font-size: 29px; line-height: 29px; color: var(--sky-text);
    text-transform: uppercase; font-weight: 400;
  }

  .concerns {
    position: absolute; left: 17px; top: 240px; width: 240px;
    list-style: none; font-size: 16px; line-height: 17px; color: var(--navy);
  }
  .concerns li { margin-bottom: 16px; }

  .badge {
    position: absolute;
    width: 118px; height: 118px; border-radius: 50%;
    background: radial-gradient(circle, var(--badge-inner) 0%, #f07a2a 60%, var(--badge-outer) 100%);
    border: 4px solid #f7b548;
    display: flex; flex-direction: column; align-items: center; justify-content: center;
    font-family: "PT Serif", Georgia, serif; font-weight: 700; color: var(--badge-text);
    text-transform: uppercase; text-align: center; line-height: 1;
  }
  .badge__small { font-size: 12.5px; }
  .badge__big { font-size: 24px; margin: 2px 0; }
  .flyer--front .badge { left: 44px; top: 411px; }
  .flyer--back .badge { left: 393px; top: 309px; }

  .front-cta {
    position: absolute; left: 220px; top: 448px; width: 295px;
    text-align: center; color: #fff; font-weight: 700; text-transform: uppercase;
    line-height: 1; text-shadow: 0 1px 2px rgba(0,0,0,.35);
  }
  .front-cta__line { display: block; font-size: 21px; }
  .front-cta__big { display: block; font-size: 29px; margin-top: 4px; }

  .testimonials { position: absolute; left: 15px; top: 553px; width: 515px; }
  .testimonials h2 { font-size: 17px; color: var(--navy); font-weight: 700; margin-left: 26px; margin-bottom: 6px; }
  .testimonials__grid {
    display: grid; grid-template-columns: 256px 250px; column-gap: 12px; row-gap: 12px;
    font-size: 12.5px; line-height: 15px; color: var(--body-text);
  }
  .quote { padding-left: 14px; position: relative; }
  .quote::before { content: "\201C"; position: absolute; left: 0; top: -2px; font-size: 20px; color: var(--navy); font-weight: 700; }
  .quote::after { content: " \201E"; font-size: 18px; color: var(--navy); font-weight: 700; }

  .rule { position: absolute; left: 15px; right: 15px; height: 1px; background: var(--rule); }
  .flyer--front .rule { top: 675px; }
  .flyer--back .rule { top: 668px; }

  .contact { position: absolute; left: 15px; font-size: 13.5px; line-height: 14.5px; color: var(--navy); }
  .contact strong { display: block; font-size: 14px; margin-bottom: 1px; }
  .flyer--front .contact { top: 683px; }
  .flyer--back .contact { top: 675px; }

  .footer-logo { position: absolute; right: 22px; display: flex; flex-direction: column; align-items: center; gap: 5px; }
  .footer-logo .logo-box__mark { width: 11px; height: 11px; }
  .footer-logo .logo-name { font-size: 13px; }
  .flyer--front .footer-logo { top: 705px; }
  .flyer--back .footer-logo { top: 690px; }

  .why {
    position: absolute; right: 15px; top: 58px; text-align: right;
    font-size: 38px; color: var(--royal); text-transform: uppercase; line-height: 1;
  }
  .why strong { font-weight: 700; }
  .credentials {
    position: absolute; right: 15px; top: 116px; width: 250px; text-align: right;
    font-size: 21px; line-height: 23px; color: #3d5fa8; list-style: none;
  }
  .credentials li + li { margin-top: 14px; }

  .specialist {
    position: absolute; left: 25px; top: 443px;
    color: #fff; font-weight: 700; font-size: 21px; text-transform: uppercase;
    text-shadow: 0 1px 2px rgba(0,0,0,.3);
  }

  .specialisms {
    position: absolute; left: 50px; top: 524px; list-style: none;
    font-size: 18.5px; line-height: 31px; color: var(--body-text);
  }
  .specialisms li { padding-left: 24px; position: relative; }
  .specialisms li::before {
    content: ""; position: absolute; left: 0; top: 11px;
    width: 9px; height: 9px; border-radius: 50%; background: var(--dot);
  }
</style>
</head>
<body>

<article class="flyer flyer--front">
  <div class="photo photo--contemplation" role="img" aria-label="Photo of a woman sitting on a mountain ledge in contemplation, looking over a valley under a blue sky"></div>

  <svg class="wave" style="top:400px;height:170px" viewBox="0 0 544 170" preserveAspectRatio="none" aria-hidden="true">
    <path d="M0 95 C160 45 340 40 544 40 L544 140 C350 130 170 155 0 165Z" fill="var(--wave-light)"/>
    <path d="M0 120 C150 70 330 50 544 35 L544 115 C360 110 180 140 0 150Z" fill="var(--wave-dark)"/>
    <path d="M0 135 C170 100 360 90 544 95 L544 125 C350 120 170 150 0 158Z" fill="var(--wave-mid)" opacity=".8"/>
    <path d="M0 158 C180 135 360 125 544 128 L544 170 L0 170Z" fill="var(--paper)"/>
  </svg>

  <div class="logo-box">
    <span class="logo-box__mark"></span>
    <span class="logo-name">TELMORA<br>COACHING</span>
  </div>

  <h1 class="headline">
    <span class="headline__lead">Do you want</span>
    <span class="headline__rest">a more fulfilling and<br>meaningful life?</span>
  </h1>

  <p class="subhead">Make this a year<br>for positive<br>change</p>

  <ul class="concerns">
    <li>I’ve lost my identity and wondering what life is about</li>
    <li>I want more intimacy in my relationship</li>
    <li>I hate my career and don’t know what’s right for me</li>
  </ul>

  <div class="badge">
    <span class="badge__small">Book your</span>
    <span class="badge__big">Free</span>
    <span class="badge__small">Consultation</span>
  </div>

  <p class="front-cta">
    <span class="front-cta__line">Personal</span>
    <span class="front-cta__line">Development Coaching</span>
    <span class="front-cta__big">Can help you!</span>
  </p>

  <section class="testimonials">
    <h2>Testimonials from our clients:</h2>
    <div class="testimonials__grid">
      <p class="quote">Coaching has helped me change the way I think, focusing more on positive rather than negative thoughts</p>
      <p class="quote">I have changed the way I approach my daily life in order to achieve more for myself</p>
      <p class="quote">Without coaching, I believe that my life would have remained stagnant</p>
      <p class="quote">Coaching has helped me to grow closer than ever to my husband</p>
    </div>
  </section>

  <div class="rule"></div>

  <address class="contact" style="font-style:normal">
    <strong>Book your free consultation:</strong>
    e: nadia@telmora-example.co.uk<br>
    t: 0798 512 6043<br>
    w: www.telmora-example.co.uk<br>
    www.facebook.com/telmora-example.co.uk<br>
    @ndtelmora
  </address>

  <div class="footer-logo">
    <span class="logo-box__mark"></span>
    <span class="logo-name">TELMORA<br>COACHING</span>
  </div>
</article>

<article class="flyer flyer--back">
  <div class="photo photo--portrait" role="img" aria-label="Portrait photo of the coach, smiling with arms folded, in front of a light staircase"></div>

  <svg class="wave" style="top:390px;height:130px" viewBox="0 0 544 130" preserveAspectRatio="none" aria-hidden="true">
    <path d="M0 40 C170 10 360 10 544 30 L544 110 C360 95 170 100 0 120Z" fill="var(--wave-light)"/>
    <path d="M0 55 C170 30 360 30 544 45 L544 100 C360 85 170 95 0 108Z" fill="var(--wave-dark)"/>
    <path d="M0 75 C180 60 360 60 544 70 L544 95 C360 85 180 100 0 105Z" fill="var(--wave-mid)" opacity=".8"/>
    <path d="M0 112 C180 92 360 88 544 100 L544 130 L0 130Z" fill="var(--paper)"/>
  </svg>

  <div class="logo-box">
    <span class="logo-box__mark"></span>
    <span class="logo-name">TELMORA<br>COACHING</span>
  </div>

  <h1 class="why">Why <strong>Telmora</strong>?</h1>

  <ul class="credentials">
    <li>Certified Personal Development Coach</li>
    <li>Experience coaching individuals wanting to effect change</li>
  </ul>

  <div class="badge">
    <span class="badge__small">Book your</span>
    <span class="badge__big">Free</span>
    <span class="badge__small">Consultation</span>
  </div>

  <h2 class="specialist">Nadia is a specialist in coaching for:</h2>

  <ul class="specialisms">
    <li>Building confidence</li>
    <li>Feeling motivated and getting out of a rut</li>
    <li>Enhancing relationships with partners or family</li>
    <li>Making changes in your career or business</li>
  </ul>

  <div class="rule"></div>

  <address class="contact" style="font-style:normal">
    <strong>Book your free consultation:</strong>
    e: nadia@telmora-example.co.uk<br>
    t: 0798 512 6043<br>
    w: www.telmora-example.co.uk<br>
    www.facebook.com/telmora-example.co.uk<br>
    @ndtelmora
  </address>

  <div class="footer-logo">
    <span class="logo-box__mark"></span>
    <span class="logo-name">TELMORA<br>COACHING</span>
  </div>
</article>

</body>
</html>
```